THE TALL COPPER ATLAS OF PORTS

subtitle: AN INTRO TO SEARCH ENGINE OPTIMIZATION
background: white
dimensions: 1562x2500

Target Market(s)

Marketing professionals

Industry/Entity Type

Digital Marketing

Font styles to use
Sans Serif

Colors
ffffff
1b1b1b
3176b5

Requirements
Should not have
• Images or graphics

```html
<!DOCTYPE html>
<html lang="en">
<head>
<meta charset="utf-8">
<title>The Tall Copper Atlas of Ports – An Intro to Search Engine Optimization</title>
<link rel="stylesheet" href="https://fonts.googleapis.com/css2?family=Oswald:wght@500;700&display=swap">
<style>
  :root {
    --paper: #ffffff;
    --ink: #1b1b1b;
    --brand-blue: #3176b5;
    --stage: #ececec;
  }
  html, body {
    margin: 0;
    padding: 0;
    width: 1200px;
    height: 1200px;
    overflow: hidden;
    background: var(--stage);
  }
  .canvas {
    position: relative;
    width: 1200px;
    height: 1200px;
  }
  .book-cover {
    position: absolute;
    left: 225px;
    top: 0;
    width: 750px;
    height: 1200px;
    background: var(--paper);
  }
  .book-cover svg {
    display: block;
    width: 750px;
    height: 1200px;
  }
  .band { fill: var(--brand-blue); }
  .title {
    font-family: "Oswald", "Arial Narrow", sans-serif;
    font-weight: 700;
  }
  .book-title {
    font-family: "Oswald", "Arial Narrow", sans-serif;
    font-weight: 500;
    fill: var(--paper);
    letter-spacing: 2px;
  }
  .title-lead { fill: var(--brand-blue); }
  .title-tag-box { fill: var(--brand-blue); }
  .title-tag-text { fill: var(--paper); }
  .initial { fill: var(--brand-blue); }
  .word-rest { fill: var(--ink); }
</style>
</head>
<body>
<main class="canvas">
  <section class="book-cover" aria-label="Book cover: The Tall Copper Atlas of Ports – An Intro to Search Engine Optimization">
    <svg viewBox="0 0 750 1200" xmlns="http://www.w3.org/2000/svg">
      <path class="band band-top" d="M0 0 H750 V95 C520 150 280 235 0 300 Z"/>
      <path class="band band-bottom" d="M0 1200 V1185 C260 1162 500 1122 750 1065 V1200 Z"/>

      <text class="book-title" x="40" y="72" font-size="40">THE TALL COPPER ATLAS OF PORTS</text>

      <g class="title">
        <text class="title-lead" x="108" y="470" font-size="115" textLength="340" lengthAdjust="spacingAndGlyphs">AN INTRO</text>

        <rect class="title-tag-box" x="462" y="362" width="148" height="118"/>
        <polygon class="title-tag-box" points="562,479 602,479 602,506"/>
        <text class="title-tag-text" x="478" y="462" font-size="115" textLength="116" lengthAdjust="spacingAndGlyphs">TO</text>

        <text class="initial" x="106" y="670" font-size="215" textLength="118" lengthAdjust="spacingAndGlyphs">S</text>
        <text class="word-rest" x="238" y="670" font-size="215" textLength="400" lengthAdjust="spacingAndGlyphs">EARCH</text>

        <text class="initial" x="112" y="865" font-size="215" textLength="108" lengthAdjust="spacingAndGlyphs">E</text>
        <text class="word-rest" x="238" y="865" font-size="215" textLength="390" lengthAdjust="spacingAndGlyphs">NGINE</text>

        <text class="initial" x="106" y="1055" font-size="215" textLength="118" lengthAdjust="spacingAndGlyphs">O</text>
        <text class="word-rest" x="238" y="1055" font-size="160" textLength="420" lengthAdjust="spacingAndGlyphs">PTIMIZATION</text>
      </g>
    </svg>
  </section>
</main>
</body>
</html>
```